Computer repair services flyer

This flyer / leaflet is required to promote my local computer and laptop repair business. It will primarily be used for pinning to notice boards when I get access to shared accommodation but I will also use it in the future for posting through letterboxes in affluent areas.

Company branding, logo, services, pricing, contact details etc. can be found on my website at : www.brightlanetech.co.uk

The services I would predominantly like to promote on this flyer are :

Speeding up slow / old computers
Virus removal
Lost data recovered
Broken laptop screen replacements
Dead laptops fixed
We buy and recycle broken laptops for cash

Other features to highlight :

Friendly and experienced
We are local (Near to Cardiff city center)
Quick repair turnaround - most repairs within 24hours
Affordable / No VAT
Free diagnostics
No Fix = No fee
Free collection and delivery
We Guarantee our work

Calls to action and attention grabbing if possible. Offer 10% off. Free cooling fan clean.

Size of flyer = A5 (210 x 148mm or 8.3 x 5.8in) portrait, single sided colour.

Target Market(s)

18 to 60 years

Industry/Entity Type

Accommodation

Requirements
Must have
• 02940 613857

```html
<!DOCTYPE html>
<html lang="en">
<head>
<meta charset="utf-8">
<title>Bright Lane Tech – Computer Repair Flyer</title>
<link rel="stylesheet" href="https://fonts.googleapis.com/css2?family=Archivo+Black&family=Arimo:ital,wght@0,400;1,400;1,700&family=Exo+2:ital,wght@1,700;1,800&display=swap">
<style>
  :root {
    --orange: #f26a1b;
    --orange-deep: #e84e0f;
    --orange-light: #ffb27a;
    --ink: #111111;
    --paper: #ffffff;
    --stripe: #e8ebec;
    --badge-red: #d9141b;
    --icon-grey: #8d8d8d;
  }
  * { box-sizing: border-box; margin: 0; padding: 0; }
  html, body { width: 900px; height: 1200px; overflow: hidden; background: var(--paper); }
  .flyer { position: relative; width: 900px; height: 1200px; background: var(--paper); overflow: hidden; font-family: "Arimo", Arial, sans-serif; color: var(--ink); }

  .side-band {
    position: absolute; left: 0; top: 0; width: 118px; height: 100%;
    background: linear-gradient(to right, var(--orange-deep) 0%, var(--orange) 55%, var(--orange-light) 88%, #fff3ea 100%);
  }
  .monitor-art {
    position: absolute; left: 0; top: 88px; width: 205px; height: 180px;
    border-radius: 10px;
    background: linear-gradient(135deg, #d7dbdf 0%, #ff8a2a 40%, #e2510c 75%, #9aa0a5 100%);
  }

  .brand { position: absolute; left: 215px; top: 40px; width: 660px; }
  .brand-name {
    font-family: "Archivo Black", "Arial Black", sans-serif;
    font-size: 92px; line-height: 0.98; letter-spacing: -2px; color: var(--ink);
  }
  .brand-tagline { margin-top: 16px; font-size: 42px; color: var(--ink); }

  .services { position: absolute; left: 50px; top: 362px; list-style: none; }
  .services li { display: flex; align-items: flex-start; height: 46px; }
  .services li.tall { height: 92px; }
  .service-mark {
    width: 64px; height: 36px; margin-right: 20px; margin-top: 4px; flex: none;
    background: linear-gradient(#f4f4f4, #b9b9b9); border: 1px solid #9a9a9a;
  }
  .service-text { font-style: italic; font-size: 37px; line-height: 46px; }

  .offer-line { position: absolute; left: 172px; top: 730px; display: flex; align-items: center; }
  .offer-text {
    margin-left: 14px; font-family: "Exo 2", sans-serif; font-style: italic; font-weight: 800;
    font-size: 36px; color: var(--orange); text-transform: uppercase;
  }
  .discount-badge { position: absolute; left: 715px; top: 668px; width: 168px; height: 168px; }

  .features { position: absolute; left: 183px; top: 826px; width: 717px; list-style: none; }
  .features li {
    display: flex; align-items: center; height: 26px; margin-bottom: 5.2px;
    background: linear-gradient(to right, var(--stripe), var(--stripe) 70%, #f7f8f8);
  }
  .features svg { margin: 0 10px 0 9px; flex: none; }
  .features span {
    font-family: "Exo 2", sans-serif; font-style: italic; font-weight: 700;
    font-size: 21px; color: var(--orange); text-transform: uppercase; white-space: nowrap;
  }

  .contact { position: absolute; left: 424px; top: 1093px; display: flex; }
  .contact-lines { margin-left: 14px; }
  .contact-phone {
    font-family: "Exo 2", sans-serif; font-style: italic; font-weight: 800;
    font-size: 52px; line-height: 52px; color: var(--orange);
  }
  .contact-web { font-size: 29px; color: var(--orange); margin-top: 6px; }
</style>
</head>
<body>
<main class="flyer">
  <div class="side-band"></div>
  <div class="monitor-art" role="img" aria-label="Illustration of a desktop computer with an orange screen"></div>

  <header class="brand">
    <h1 class="brand-name">Bright Lane<br>Tech</h1>
    <p class="brand-tagline">and your laptop too!</p>
  </header>

  <ul class="services">
    <li><span class="service-mark"></span><span class="service-text">Speeding up slow / old computers</span></li>
    <li><span class="service-mark"></span><span class="service-text">Virus removal</span></li>
    <li><span class="service-mark"></span><span class="service-text">Lost data recovered</span></li>
    <li><span class="service-mark"></span><span class="service-text">Broken laptop screen replacements</span></li>
    <li><span class="service-mark"></span><span class="service-text">Dead laptops fixed</span></li>
    <li class="tall"><span class="service-mark"></span><span class="service-text">We buy and recycle broken laptops<br>for cash</span></li>
  </ul>

  <div class="offer-line">
    <svg width="44" height="44" viewBox="0 0 44 44" aria-hidden="true">
      <circle cx="22" cy="22" r="20" fill="#f4f4f4" stroke="var(--icon-grey)" stroke-width="2"/>
      <path d="M15 12 L31 22 L15 32 L19 22 Z" fill="var(--icon-grey)"/>
    </svg>
    <span class="offer-text">Free cooling fan clean!</span>
  </div>

  <svg class="discount-badge" viewBox="0 0 168 168" aria-label="10% exclusive discount">
    <polygon fill="var(--badge-red)" points="84,4 97,22 118,13 122,35 145,36 138,58 158,70 142,86 155,105 133,112 135,135 112,132 103,153 84,140 65,153 56,132 33,135 35,112 13,105 26,86 10,70 30,58 23,36 46,35 50,13 71,22"/>
    <text x="84" y="72" text-anchor="middle" font-family="Archivo Black, sans-serif" font-size="38" fill="#fff" transform="rotate(-8 84 84)">10%</text>
    <text x="84" y="96" text-anchor="middle" font-family="Arimo, sans-serif" font-weight="700" font-size="15" fill="#fff" transform="rotate(-8 84 84)">EXCLUSIVE</text>
    <text x="84" y="115" text-anchor="middle" font-family="Arimo, sans-serif" font-weight="700" font-size="15" fill="#fff" transform="rotate(-8 84 84)">DISCOUNT</text>
  </svg>

  <ul class="features">
    <li><svg width="18" height="18" viewBox="0 0 18 18"><circle cx="9" cy="9" r="8" fill="none" stroke="var(--orange)" stroke-width="1.6"/><path d="M9 5v8M5 9h8" stroke="var(--orange)" stroke-width="1.8"/></svg><span>Friendly and experienced</span></li>
    <li><svg width="18" height="18" viewBox="0 0 18 18"><circle cx="9" cy="9" r="8" fill="none" stroke="var(--orange)" stroke-width="1.6"/><path d="M9 5v8M5 9h8" stroke="var(--orange)" stroke-width="1.8"/></svg><span>We are local (near to Cardiff city center)</span></li>
    <li><svg width="18" height="18" viewBox="0 0 18 18"><circle cx="9" cy="9" r="8" fill="none" stroke="var(--orange)" stroke-width="1.6"/><path d="M9 5v8M5 9h8" stroke="var(--orange)" stroke-width="1.8"/></svg><span>Quick repair turnaround – most repairs within 24hours</span></li>
    <li><svg width="18" height="18" viewBox="0 0 18 18"><circle cx="9" cy="9" r="8" fill="none" stroke="var(--orange)" stroke-width="1.6"/><path d="M9 5v8M5 9h8" stroke="var(--orange)" stroke-width="1.8"/></svg><span>Affordable / No VAT</span></li>
    <li><svg width="18" height="18" viewBox="0 0 18 18"><circle cx="9" cy="9" r="8" fill="none" stroke="var(--orange)" stroke-width="1.6"/><path d="M9 5v8M5 9h8" stroke="var(--orange)" stroke-width="1.8"/></svg><span>Free diagnostics</span></li>
    <li><svg width="18" height="18" viewBox="0 0 18 18"><circle cx="9" cy="9" r="8" fill="none" stroke="var(--orange)" stroke-width="1.6"/><path d="M9 5v8M5 9h8" stroke="var(--orange)" stroke-width="1.8"/></svg><span>No fix = No fee</span></li>
    <li><svg width="18" height="18" viewBox="0 0 18 18"><circle cx="9" cy="9" r="8" fill="none" stroke="var(--orange)" stroke-width="1.6"/><path d="M9 5v8M5 9h8" stroke="var(--orange)" stroke-width="1.8"/></svg><span>Free collection and delivery</span></li>
    <li><svg width="18" height="18" viewBox="0 0 18 18"><circle cx="9" cy="9" r="8" fill="none" stroke="var(--orange)" stroke-width="1.6"/><path d="M9 5v8M5 9h8" stroke="var(--orange)" stroke-width="1.8"/></svg><span>We guarantee our work</span></li>
  </ul>

  <footer class="contact">
    <svg width="86" height="86" viewBox="0 0 86 86" aria-hidden="true">
      <circle cx="43" cy="43" r="38" fill="none" stroke="var(--orange)" stroke-width="7"/>
      <path d="M30 22c3-2 6-1 7 2l3 8c1 2 0 4-2 5l-3 2c2 6 7 11 13 13l2-3c1-2 3-3 5-2l8 3c3 1 4 4 2 7l-3 4c-3 3-8 4-13 2-12-5-21-14-26-26-2-5-1-10 2-13z" fill="var(--orange)"/>
    </svg>
    <div class="contact-lines">
      <p class="contact-phone">02940 613857</p>
      <p class="contact-web">www.brightlanetech.co.uk</p>
    </div>
  </footer>
</main>
</body>
</html>
```